Stationery modern simple design
Corporate Stationery
Project: Stationery modern simple design
Creative Brief
Simple
Faisal Alqurashi
General Manager
Sable Grid Company 3858 Nakheel Crest Rd Wardah Tower Riyadh 13847 Saudi Arabia
info@sablegrid.example
www.sablegrid.example
address will be not use in business card and will be used in any other Stationery Arabic Address: شركة سابل جريد ٣٨٥٨ طريق النخيل الأعلى الرياض ١٣٨٤٧ المملكة العربية السعودية
فيصل القرشي المدير العام infor@sablegrid.example +966117290813 +9665031476095

```html
<!DOCTYPE html>
<html lang="en">
<head>
<meta charset="utf-8">
<title>Sable Grid – Business Card</title>
<link rel="stylesheet" href="https://fonts.googleapis.com/css2?family=Montserrat:wght@400;500;600;700&family=Cairo:wght@500;600&display=swap">
<style>
  :root {
    --backdrop: #2a2b2e;
    --card-dark: #1d1e20;
    --card-white: #ffffff;
    --brand-blue: #1f8ad6;
    --brand-blue-deep: #136fb5;
    --ink: #3b3f45;
    --ink-soft: #6b7078;
    --on-blue: #ffffff;
    --on-dark: #d9dbde;
  }
  * { margin: 0; padding: 0; box-sizing: border-box; }
  html, body { width: 1200px; height: 689px; overflow: hidden; }
  body {
    background: var(--backdrop);
    font-family: "Montserrat", sans-serif;
    display: flex;
    align-items: center;
    justify-content: center;
    gap: 60px;
  }
  .card {
    width: 500px;
    height: 286px;
    border-radius: 14px;
    overflow: hidden;
    position: relative;
    box-shadow: 0 18px 40px rgba(0,0,0,.45);
  }

  /* Front */
  .card-front {
    background: var(--card-dark);
    display: flex;
    flex-direction: column;
    align-items: center;
    justify-content: center;
  }
  .brand {
    display: flex;
    align-items: center;
    gap: 10px;
    font-weight: 600;
    letter-spacing: 2px;
    color: var(--brand-blue);
    text-transform: uppercase;
  }
  .brand-square {
    width: 14px; height: 14px;
    background: var(--brand-blue);
  }
  .card-front .brand { font-size: 30px; }
  .card-front .brand-square { width: 22px; height: 22px; }
  .front-url {
    margin-top: 44px;
    font-size: 12px;
    color: var(--on-dark);
    letter-spacing: .5px;
  }

  /* Back */
  .card-back {
    background: var(--card-white);
    display: grid;
    grid-template-columns: 1fr 1fr;
  }
  .card-back::after {
    content: "";
    position: absolute;
    left: 0; right: 0; bottom: 0;
    height: 47%;
    background: linear-gradient(180deg, var(--brand-blue), var(--brand-blue-deep));
    z-index: 0;
  }
  .identity, .contact { position: relative; z-index: 1; }
  .identity {
    display: flex;
    flex-direction: column;
    justify-content: space-between;
    padding: 52px 0 22px 30px;
  }
  .card-back .brand { font-size: 21px; }
  .person { color: var(--on-blue); }
  .person-name { font-size: 17px; font-weight: 700; }
  .person-name-ar {
    font-family: "Cairo", sans-serif;
    font-size: 13px;
    font-weight: 600;
    direction: rtl;
    text-align: left;
    margin-top: 2px;
  }
  .person-title { font-size: 11px; font-weight: 500; margin-top: 1px; }
  .person-email { font-size: 11px; margin-top: 4px; }

  .contact {
    padding: 30px 26px 22px 22px;
    border-left: 1px solid #d5d8dc;
    margin: 22px 0;
    display: flex;
    flex-direction: column;
    justify-content: space-between;
  }
  .contact-row {
    display: flex;
    gap: 10px;
    align-items: flex-start;
    font-size: 11px;
    line-height: 1.45;
  }
  .contact-row svg { flex: none; width: 13px; height: 13px; margin-top: 2px; }
  .contact-address { color: var(--ink); }
  .contact-address svg { fill: var(--brand-blue); }
  .contact-list { display: flex; flex-direction: column; gap: 5px; color: var(--on-blue); }
  .contact-list svg { fill: var(--on-blue); }
</style>
</head>
<body>

  <section class="card card-front">
    <div class="brand"><span class="brand-square"></span>Sable Grid</div>
    <p class="front-url">www.sablegrid.example</p>
  </section>

  <section class="card card-back">
    <div class="identity">
      <div class="brand"><span class="brand-square"></span>Sable Grid</div>
      <div class="person">
        <p class="person-name">Faisal Alqurashi</p>
        <p class="person-name-ar" lang="ar">فيصل القرشي · المدير العام</p>
        <p class="person-title">General Manager</p>
        <p class="person-email">info@sablegrid.example</p>
      </div>
    </div>

    <div class="contact">
      <div class="contact-row contact-address">
        <svg viewBox="0 0 24 24" aria-hidden="true"><path d="M12 2a7 7 0 0 0-7 7c0 5.2 7 13 7 13s7-7.8 7-13a7 7 0 0 0-7-7zm0 9.5a2.5 2.5 0 1 1 0-5 2.5 2.5 0 0 1 0 5z"/></svg>
        <p>3858 Nakheel Crest Rd<br>Wardah Tower Riyadh 13847<br>Saudi Arabia</p>
      </div>
      <div class="contact-list">
        <div class="contact-row">
          <svg viewBox="0 0 24 24" aria-hidden="true"><path d="M6.6 10.8a15 15 0 0 0 6.6 6.6l2.2-2.2a1 1 0 0 1 1-.25 11.4 11.4 0 0 0 3.6.57 1 1 0 0 1 1 1V20a1 1 0 0 1-1 1A17 17 0 0 1 3 4a1 1 0 0 1 1-1h3.5a1 1 0 0 1 1 1c0 1.25.2 2.45.57 3.6a1 1 0 0 1-.25 1z"/></svg>
          <p>+966117290813</p>
        </div>
        <div class="contact-row">
          <svg viewBox="0 0 24 24" aria-hidden="true"><path d="M16 1H8a2 2 0 0 0-2 2v18a2 2 0 0 0 2 2h8a2 2 0 0 0 2-2V3a2 2 0 0 0-2-2zm-4 21a1.3 1.3 0 1 1 0-2.6 1.3 1.3 0 0 1 0 2.6zm4-4H8V4h8z"/></svg>
          <p>+9665031476095</p>
        </div>
        <div class="contact-row">
          <svg viewBox="0 0 24 24" aria-hidden="true"><path d="M12 2a10 10 0 1 0 0 20 10 10 0 0 0 0-20zm6.9 6h-3a15.7 15.7 0 0 0-1.4-3.6A8 8 0 0 1 18.9 8zM12 4a14 14 0 0 1 1.9 4h-3.8A14 14 0 0 1 12 4zM4.3 14a8 8 0 0 1 0-4h3.4a16 16 0 0 0 0 4zm.8 2h3a15.7 15.7 0 0 0 1.4 3.6A8 8 0 0 1 5.1 16zm3-8h-3a8 8 0 0 1 4.4-3.6A15.7 15.7 0 0 0 8.1 8zM12 20a14 14 0 0 1-1.9-4h3.8A14 14 0 0 1 12 20zm2.3-6H9.7a14.7 14.7 0 0 1 0-4h4.6a14.7 14.7 0 0 1 0 4zm.3 5.6a15.7 15.7 0 0 0 1.4-3.6h3a8 8 0 0 1-4.4 3.6zm1.7-5.6a16 16 0 0 0 0-4h3.4a8 8 0 0 1 0 4z"/></svg>
          <p>www.sablegrid.example</p>
        </div>
      </div>
    </div>
  </section>

</body>
</html>
```